LoweniasMassage website required

We need a website for a mobile sports massage therapist in the United Kingdom. Specialising in pregnancy and postnatal massage, sports and remedial, deep tissue massage & Corprate Massage. Attached are some logos that we already have in various colours. The file named logo_white_background is what we normally use. Feel free to use the others at your discretion.

Requirements
Must have
• Service areas, Booking system.

```html
<!DOCTYPE html>
<html lang="en">
<head>
<meta charset="utf-8">
<title>Lowenias Massage</title>
<link rel="stylesheet" href="https://fonts.googleapis.com/css2?family=Roboto+Condensed:wght@400;700&family=Open+Sans:ital,wght@0,400;0,600;0,700;1,400&family=Lato:ital,wght@0,400;0,700;1,400&display=swap">
<style>
:root{
  --green:#8cc63f;
  --green-dark:#7ab52f;
  --navy:#0b3a57;
  --ink:#2b2b2b;
  --text:#555555;
  --muted:#888888;
  --grey-band:#e7e7e7;
  --footer:#333333;
  --white:#ffffff;
  --line:#dddddd;
}
*{box-sizing:border-box;margin:0;padding:0}
html,body{width:1200px;height:2469px;overflow:hidden}
body{position:relative;background:var(--white);font-family:"Open Sans",sans-serif;color:var(--text)}
.abs{position:absolute}
.center{text-align:center}

/* hero */
.hero{left:0;top:0;width:1200px;height:502px;background:linear-gradient(100deg,#4a4946 0%,#6d6a66 35%,#3d3c3b 60%,#807c76 80%,#5b5752 100%)}
.hero-shade{left:0;top:0;width:1200px;height:502px;background:rgba(20,20,20,.35)}
.logo-box{left:173px;top:0;width:123px;height:110px;background:var(--white);display:flex;align-items:center;justify-content:center;text-align:center;font-family:"Lato",sans-serif;font-size:15px;font-weight:700;color:#3fa9d6;line-height:1.2;padding:0 8px}
.main-nav{left:459px;top:21px;width:413px;height:42px;background:var(--navy);display:flex;align-items:center;justify-content:space-around;padding:0 10px}
.main-nav a{color:var(--white);font-family:"Open Sans",sans-serif;font-size:12px;font-weight:600;text-decoration:none}
.nav-phone{left:892px;top:21px;width:133px;height:42px;background:var(--green);display:flex;align-items:center;justify-content:center;gap:10px;color:var(--white);font-size:13px}
.hero-tag{left:520px;top:179px;width:160px;height:42px;background:var(--green);color:var(--white);font-family:"Roboto Condensed",sans-serif;font-weight:700;font-size:20px;display:flex;align-items:center;justify-content:center;border-radius:2px}
.hero-title{left:0;top:244px;width:1200px;font-family:"Roboto Condensed",sans-serif;font-weight:700;font-size:46px;color:var(--white);text-align:center}
.hero-text{left:250px;top:306px;width:700px;font-size:12.5px;line-height:24px;color:var(--white);text-align:center}

/* about */
.about-accent{width:50px;height:50px;background:var(--green)}
.about-photo{left:209px;top:561px;width:389px;height:346px;background:linear-gradient(160deg,#dfe9ec,#a9c0c6 55%,#c9d8dc);border-radius:3px}
.about-title{left:640px;top:562px;font-family:"Roboto Condensed",sans-serif;font-weight:700;font-size:36px;color:var(--ink)}
.about-sub{left:640px;top:619px;font-style:italic;font-size:15px;color:var(--green)}
.about-text{left:640px;top:656px;width:385px;font-size:12.5px;line-height:24.3px;text-align:justify}
.btn-video{left:640px;top:844px;width:137px;height:37px;background:var(--green);color:var(--white);border-radius:3px;font-size:15px;display:flex;align-items:center;justify-content:center;gap:8px}

/* section heads */
.section-title{left:0;width:1200px;text-align:center;font-family:"Roboto Condensed",sans-serif;font-weight:700;font-size:31px;color:var(--ink)}
.section-rule{left:584px;width:32px;height:3px;background:var(--ink)}
.section-sub{left:400px;width:400px;text-align:center;font-size:11.5px;line-height:20px;color:#444}

/* services */
.service{top:1123px;width:270px;height:362px;border:1px solid var(--green)}
.service.is-featured{background:var(--green)}
.service-card{position:absolute;left:15px;top:15px;right:15px;bottom:15px;background:var(--white);box-shadow:0 3px 8px rgba(0,0,0,.18);text-align:center}
.service-photo{position:absolute;left:28px;top:22px;width:185px;height:122px}
.service-name{position:absolute;left:0;top:170px;width:100%;font-size:12.5px;font-weight:600;color:var(--ink)}
.service-rule{position:absolute;left:106px;top:197px;width:28px;height:2px;background:var(--ink)}
.service-text{position:absolute;left:24px;top:208px;width:192px;font-size:13px;line-height:20px;color:#444}
.btn-details{position:absolute;left:75px;top:287px;width:89px;height:28px;border:1px solid var(--green);border-radius:14px;font-size:9.5px;color:var(--green);display:flex;align-items:center;justify-content:center}
.is-featured .btn-details{background:var(--green);color:var(--white)}

/* team */
.member{top:1671px;width:196px;height:258px;text-align:center}
.member-photo{width:196px;height:194px;background:linear-gradient(180deg,#e9e9e9,#cfd4d8)}
.member-name{position:absolute;left:0;top:212px;width:100%;font-size:13.5px;color:var(--ink)}
.member-role{position:absolute;left:0;top:234px;width:100%;font-size:8.5px;color:var(--muted)}
.member-rule{position:absolute;left:8px;bottom:0;width:180px;height:1px;background:#e4e4e4}
.member.is-active .member-info{position:absolute;left:0;top:194px;width:196px;height:64px;background:#34363f}
.member.is-active .member-name,.member.is-active .member-role{color:var(--white)}
.member-social{position:absolute;left:0;top:169px;width:196px;height:25px;background:var(--green);display:flex;align-items:center;justify-content:center;gap:16px}
.member-social span{width:7px;height:7px;border-radius:50%;background:var(--white)}

/* commitment / testimonials */
.band{left:0;top:1985px;width:1200px;height:324px;background:var(--grey-band)}
.band-title{font-family:"Roboto Condensed",sans-serif;font-weight:700;font-size:21px;color:var(--ink)}
.band-title em{font-style:normal;color:var(--green)}
.commit-text{left:157px;top:2073px;width:420px;font-size:13px;line-height:23px;color:#333}
.commit-list{left:155px;top:2150px;list-style:none}
.commit-list li{display:flex;align-items:center;gap:8px;height:31px;font-size:13px;color:#333}
.band-divider{left:594px;top:2030px;width:1px;height:255px;background:#cfcfcf}
.slider-btn{top:2025px;width:24px;height:23px;background:var(--white);border:1px solid #ccc;display:flex;align-items:center;justify-content:center}
.quote{left:625px;top:2077px;width:407px;height:120px;background:var(--white);border-radius:6px;padding:14px 18px 0 26px;font-family:"Lato",sans-serif;font-style:italic;font-size:11.5px;line-height:20px;color:#333}
.quote-mark{left:640px;top:2079px;font-family:Georgia,serif;font-size:30px;color:#bbb}
.avatar{left:645px;top:2225px;width:60px;height:60px;border-radius:50%;background:linear-gradient(135deg,#8b8b8b,#3e3e3e)}
.client-name{left:724px;top:2245px;font-size:11px;font-weight:600;color:var(--green)}

/* footer */
.foot-nav{left:0;top:2309px;width:1200px;height:61px;background:var(--green)}
.foot-links{left:156px;top:2332px;display:flex;gap:0;font-size:14px;color:var(--white)}
.foot-links span.sep{padding:0 16px}
.follow{left:856px;top:2327px;font-size:20px;color:var(--white);font-weight:600}
.follow-dot{top:2325px;width:30px;height:30px;border-radius:50%;background:var(--white)}
.foot-base{left:0;top:2370px;width:1200px;height:99px;background:var(--footer)}
.foot-icon{top:2402px;width:28px;height:28px;border-radius:50%;background:var(--green);display:flex;align-items:center;justify-content:center}
.foot-label{top:2400px;font-size:14px;color:var(--white)}
.foot-small{top:2420px;font-size:9.5px;color:#ccc}
.foot-brand{left:815px;top:2388px;width:205px;text-align:center;font-family:"Roboto Condensed",sans-serif;font-weight:700;font-size:22px;color:var(--white)}
.foot-copy{left:815px;width:205px;text-align:center;font-size:10.5px;font-weight:600;color:var(--white)}
</style>
</head>
<body>

<!-- hero -->
<div class="abs hero" role="img" aria-label="Blurred photo of a runner's legs on a track"></div>
<div class="abs hero-shade"></div>
<div class="abs logo-box">Lowenias Massage</div>
<nav class="abs main-nav">
  <a>HOME</a><a>ABOUT US</a><a>SERVICES ▾</a><a>INQUIRY</a><a>CONTACT US</a>
</nav>
<div class="abs nav-phone">
  <svg width="18" height="14" viewBox="0 0 18 14"><path d="M2 4 Q9 -1 16 4 L14 6 L12 4.5 L12 3 Q9 2 6 3 L6 4.5 L4 6 Z M4 7 H14 L15 13 H3 Z" fill="#fff"/></svg>
  <span>123 456 789</span>
</div>
<div class="abs hero-tag">Specialising in</div>
<h1 class="abs hero-title">PREGNANCY AND POSTNATAL MASSAGE</h1>
<p class="abs hero-text">Sed ut perspiciatis unde omnis iste natus error sit voluptatem accusantium doloremque laudantium, totam rem aperiam, eaque ipsa quae ab illo inventore veritatis et quasi veritatis et quasi architecto beatae vitae dicta sunt explicabo. Sed ut perspiciatis unde omnis iste natus error.</p>

<!-- about -->
<div class="abs about-accent" style="left:194px;top:546px"></div>
<div class="abs about-accent" style="left:565px;top:874px"></div>
<div class="abs about-photo" role="img" aria-label="Photo of clinicians in white coats walking down a bright corridor"></div>
<h2 class="abs about-title">LOWENIAS MASSAGE</h2>
<p class="abs about-sub">Sed ut perspiciatis unde omnis</p>
<p class="abs about-text">Sed ut perspiciatis unde omnis iste natus error sit voluptatem accusantium doloremque laudantium, totam rem aperiam, eaque ipsa quae ab illo inventore veritatis et quasi veritatis et quasi architecto beatae vitae dicta sunt explicabo. Sed ut perspiciatis unde omnis iste natus error.<br>Sed ut perspiciatis unde omnis iste natus error sit voluptatem accusantium doloremque laudantium.</p>
<div class="abs btn-video">Watch Video
  <svg width="14" height="14" viewBox="0 0 14 14"><circle cx="7" cy="7" r="6" fill="none" stroke="#fff" stroke-width="1.2"/><path d="M5.5 4.2 L9.8 7 L5.5 9.8 Z" fill="#fff"/></svg>
</div>

<!-- services -->
<h2 class="abs section-title" style="top:981px">SERVICES</h2>
<div class="abs section-rule" style="top:1032px"></div>
<p class="abs section-sub" style="top:1040px">Sed ut perspiciatis unde omnis iste natus error sitvoluptatem accusantium doloremque laudantium.</p>

<div class="abs service" style="left:173px">
  <div class="service-card">
    <div class="service-photo" role="img" aria-label="Photo of women stretching in a yoga class" style="background:linear-gradient(135deg,#e9e4e6,#d68fb6 60%,#c9b7bf)"></div>
    <div class="service-name">Pregnancy and Postnatal Massage</div>
    <div class="service-rule"></div>
    <p class="service-text">Lorem ipsum dolor sit amet, con-sectetuer adipiscing elit, dolore magna aliquam erat volutpat..</p>
    <div class="btn-details">View Details</div>
  </div>
</div>
<div class="abs service is-featured" style="left:466px">
  <div class="service-card">
    <div class="service-photo" role="img" aria-label="Photo of two runners on a seaside promenade" style="background:linear-gradient(180deg,#b9d3e6,#7f8f99 55%,#9a8a7c)"></div>
    <div class="service-name">Sports and Remedial</div>
    <div class="service-rule"></div>
    <p class="service-text">Lorem ipsum dolor sit amet, con-sectetuer adipiscing elit, dolore magna aliquam erat volutpat..</p>
    <div class="btn-details">View Details</div>
  </div>
</div>
<div class="abs service" style="left:757px">
  <div class="service-card">
    <div class="service-photo" role="img" aria-label="Photo of hands massaging a client's leg" style="background:linear-gradient(135deg,#f3ece6,#d4a287 55%,#8a5a44)"></div>
    <div class="service-name">Deep Tissue &amp; Corprate Massage</div>
    <div class="service-rule"></div>
    <p class="service-text">Lorem ipsum dolor sit amet, con-sectetuer adipiscing elit, dolore magna aliquam erat volutpat..</p>
    <div class="btn-details">View Details</div>
  </div>
</div>

<!-- speciality / team -->
<h2 class="abs section-title" style="top:1531px">OUR SPECIALITY</h2>
<div class="abs section-rule" style="top:1581px"></div>
<p class="abs section-sub" style="top:1590px">Sed ut perspiciatis unde omnis iste natus error sitvoluptatem accusantium doloremque laudantium.</p>

<div class="abs member" style="left:173px">
  <div class="member-photo" role="img" aria-label="Portrait photo of a therapist in a blue shirt"></div>
  <div class="member-name">Member Name</div>
  <div class="member-role">Pregnancy and Postnatal Massage</div>
  <div class="member-rule"></div>
</div>
<div class="abs member is-active" style="left:392px">
  <div class="member-photo" role="img" aria-label="Portrait photo of a therapist in a suit"></div>
  <div class="member-social"><span></span><span></span><span></span><span></span></div>
  <div class="member-info"></div>
  <div class="member-name">Member Name</div>
  <div class="member-role">Sports and Remedial</div>
</div>
<div class="abs member" style="left:611px">
  <div class="member-photo" role="img" aria-label="Portrait photo of a therapist in a blue shirt"></div>
  <div class="member-name">Member Name</div>
  <div class="member-role">Deep Tissue &amp; Corprate Massage</div>
  <div class="member-rule"></div>
</div>
<div class="abs member" style="left:830px">
  <div class="member-photo" role="img" aria-label="Portrait photo of a therapist in a checked shirt"></div>
  <div class="member-name">Member Name</div>
  <div class="member-role">Sports and Remedial</div>
  <div class="member-rule"></div>
</div>

<!-- commitment & testimonials -->
<div class="abs band"></div>
<h3 class="abs band-title" style="left:153px;top:2022px">OUR <em>COMMITMENT TO CUSTOMERS</em></h3>
<p class="abs commit-text">Loren autem vel eum iriure hendrerit in vulputate velit esse molestie. onsectetuer adipiscing elit, sed diam nonummy nibh euismod tincidunt u eu feugiat nulla facilisis.</p>
<ul class="abs commit-list">
  <li><svg width="14" height="14" viewBox="0 0 14 14"><circle cx="7" cy="7" r="7" fill="#8cc63f"/><path d="M3.8 7.2 L6 9.3 L10.2 4.9" stroke="#fff" stroke-width="1.6" fill="none"/></svg>Autem vel eum iriure hendrerit in</li>
  <li><svg width="14" height="14" viewBox="0 0 14 14"><circle cx="7" cy="7" r="7" fill="#8cc63f"/><path d="M3.8 7.2 L6 9.3 L10.2 4.9" stroke="#fff" stroke-width="1.6" fill="none"/></svg>Gendrerit in vulputate velit</li>
  <li><svg width="14" height="14" viewBox="0 0 14 14"><circle cx="7" cy="7" r="7" fill="#8cc63f"/><path d="M3.8 7.2 L6 9.3 L10.2 4.9" stroke="#fff" stroke-width="1.6" fill="none"/></svg>Autem vel eum adipiscing elit, sed diam</li>
  <li><svg width="14" height="14" viewBox="0 0 14 14"><circle cx="7" cy="7" r="7" fill="#8cc63f"/><path d="M3.8 7.2 L6 9.3 L10.2 4.9" stroke="#fff" stroke-width="1.6" fill="none"/></svg>Eeum iriure hendrerit in vulputate velit</li>
</ul>
<div class="abs band-divider"></div>

<h3 class="abs band-title" style="left:625px;top:2022px">CLIENT <em>TESTIMONIALS</em></h3>
<div class="abs slider-btn" style="left:979px"><svg width="8" height="10" viewBox="0 0 8 10"><path d="M6 1 L2 5 L6 9" stroke="#555" stroke-width="1.5" fill="none"/></svg></div>
<div class="abs slider-btn" style="left:1007px"><svg width="8" height="10" viewBox="0 0 8 10"><path d="M2 1 L6 5 L2 9" stroke="#555" stroke-width="1.5" fill="none"/></svg></div>
<div class="abs quote">Lorem ipsum dolor sit amet consetug e sed diay nibh euismodl tincidunt ut laoreet dolore magam er vol wisi enim ad minim veniam quis nostrud exerci tationorem ipsum dolor sit ametee sed diammmy nibh euismd tincidunt ut laoreet dolore magna aliqur volpatl tiidunt ut laoreet dolore magna aliqur volpatl r sit ametee.</div>
<div class="abs quote-mark">“</div>
<svg class="abs" style="left:920px;top:2196px" width="40" height="26" viewBox="0 0 40 26"><path d="M0 0 H40 L2 26 Z" fill="#fff"/></svg>
<div class="abs avatar" role="img" aria-label="Client portrait photo"></div>
<div class="abs client-name">Mr. Dorian Pell</div>

<!-- footer -->
<div class="abs foot-nav"></div>
<div class="abs foot-links">
  <span>HOME</span><span class="sep">|</span><span>ABOUT US</span><span class="sep">|</span><span>SERVICES</span><span class="sep">|</span><span>INQUIRY</span><span class="sep">|</span><span>CONTACT US</span>
</div>
<div class="abs follow">Follow Us:</div>
<div class="abs follow-dot" style="left:964px"></div>
<div class="abs follow-dot" style="left:1002px"></div>

<div class="abs foot-base"></div>
<div class="abs foot-icon" style="left:156px"><svg width="12" height="15" viewBox="0 0 12 15"><path d="M6 0 A5.5 5.5 0 0 1 11.5 5.5 C11.5 9 6 15 6 15 C6 15 0.5 9 0.5 5.5 A5.5 5.5 0 0 1 6 0 Z" fill="#fff"/><circle cx="6" cy="5.5" r="2" fill="#8cc63f"/></svg></div>
<div class="abs foot-label" style="left:194px">Lowenias Massage</div>
<div class="abs foot-small" style="left:194px">Your Company Address</div>
<div class="abs foot-icon" style="left:404px"><svg width="14" height="14" viewBox="0 0 14 14"><path d="M3 1 L5.5 3.8 L4.2 5.6 Q5.8 8.4 8.4 9.8 L10.2 8.5 L13 11 L11.3 13 Q5 12.5 1 3 Z" fill="#fff"/></svg></div>
<div class="abs foot-label" style="left:443px">Call Us :</div>
<div class="abs foot-small" style="left:443px">123.456.789</div>
<div class="abs foot-icon" style="left:584px"><svg width="14" height="11" viewBox="0 0 14 11"><rect x="0.5" y="0.5" width="13" height="10" fill="#fff"/><path d="M1 1 L7 6 L13 1" stroke="#8cc63f" stroke-width="1.3" fill="none"/></svg></div>
<div class="abs foot-label" style="left:622px">Email Us :</div>
<div class="abs foot-small" style="left:622px">info@lowenias-example.com</div>
<div class="abs foot-brand">LOWENIAS MASSAGE</div>
<div class="abs foot-copy" style="top:2418px">© 2018 Lowenias Massage.</div>
<div class="abs foot-copy" style="top:2437px">All Rights Reserved.</div>

</body>
</html>
```